Marketing Flyer

I need a flyer for my marketing company. I would like for it to to be consistent with my logo and business card design. I would also like for there to be an image of a crowded waiting room, or restaurant with people gathered around a flat screen that reads "Your Ad Here".

Requirements
Must have
• logo, info on attached doc.
Nice to have
• Possibly a picture people in a waiting room or restaurant with a digital sign present that reads "your ad here".

```html
<!DOCTYPE html>
<html lang="en">
<head>
<meta charset="utf-8">
<title>FieldLine Marketing Flyer</title>
<link rel="stylesheet" href="https://fonts.googleapis.com/css2?family=Open+Sans:wght@400;600;700;800&family=Ubuntu:wght@700&display=swap">
<style>
  :root {
    --page-bg: #ececec;
    --paper: #ffffff;
    --brand-green: #8dc03a;
    --band-green: #93c01f;
    --ink: #1b1b1b;
    --grey-title: #5f5f5f;
    --photo-dark: #1d2433;
    --photo-mid: #5b6677;
    --photo-light: #c9ccd0;
  }
  * { box-sizing: border-box; margin: 0; padding: 0; }
  html, body { width: 716px; height: 1200px; overflow: hidden; }
  body {
    background: var(--page-bg);
    font-family: "Open Sans", Arial, sans-serif;
    color: var(--ink);
    position: relative;
  }
  .flyer {
    position: absolute;
    left: 0; top: 94px;
    width: 716px; height: 1012px;
    background: var(--paper);
    box-shadow: 0 8px 22px rgba(0,0,0,0.35);
    overflow: hidden;
  }
  .header { position: relative; height: 115px; }
  .brand {
    position: absolute; left: 41px; top: 24px;
    color: var(--grey-title);
    font-weight: 700;
    display: flex; align-items: center; gap: 10px;
  }
  .brand-dot {
    width: 22px; height: 22px; border-radius: 50%;
    background: var(--brand-green);
  }
  .brand-name { font-size: 44px; line-height: 46px; letter-spacing: -0.5px; }
  .brand-tag { font-size: 15px; letter-spacing: 6px; line-height: 18px; }
  .divider {
    position: absolute; left: 462px; top: 22px;
    width: 3px; height: 76px; background: var(--brand-green);
  }
  .contacts { position: absolute; left: 494px; top: 24px; list-style: none; }
  .contacts li {
    display: flex; align-items: center; gap: 9px;
    font-size: 15.5px; height: 25px;
  }
  .contacts svg { width: 14px; height: 14px; flex: none; }
  .contacts b { font-weight: 700; }

  .hero { position: relative; height: 430px; }
  .hero-photo {
    position: absolute; inset: 0;
    background:
      radial-gradient(ellipse at 55% 25%, rgba(240,236,228,0.85), transparent 45%),
      radial-gradient(ellipse at 40% 85%, var(--photo-light), transparent 50%),
      linear-gradient(110deg, var(--photo-dark) 0%, var(--photo-mid) 45%, #2a3550 75%, var(--photo-dark) 100%);
  }
  .hero-panel {
    position: absolute; left: 41px; top: 0;
    width: 285px; height: 340px;
    background: rgba(141,192,58,0.95);
    padding: 64px 0 0 29px;
    color: var(--ink);
  }
  .hero-panel p { font-size: 37px; line-height: 54px; font-weight: 400; }
  .hero-panel strong {
    display: block; color: #fff; font-weight: 800;
    font-size: 47px; line-height: 52px;
  }

  .benefits { padding: 28px 54px 0 39px; }
  .benefits h2 {
    font-family: "Ubuntu", "Open Sans", sans-serif;
    font-size: 30px; color: var(--grey-title); font-weight: 700;
    margin-bottom: 12px;
  }
  .benefit-list { list-style: none; }
  .benefit-list li {
    position: relative; padding-left: 24px;
    font-size: 15.3px; line-height: 21.5px;
    text-align: justify; margin-bottom: 7px;
  }
  .benefit-list li::before {
    content: "\2713"; position: absolute; left: 2px; top: 0;
    font-size: 15px;
  }
  .benefit-list b { font-weight: 700; }

  .footer-band {
    position: absolute; left: 0; bottom: 0;
    width: 100%; height: 54px;
    background: var(--band-green);
    display: flex; align-items: center; justify-content: center;
    font-size: 17px; letter-spacing: 5px; color: var(--ink);
  }
  .footer-band b { font-weight: 800; }
</style>
</head>
<body>
  <main class="flyer">
    <header class="header">
      <div class="brand">
        <span class="brand-dot"></span>
        <div>
          <div class="brand-name">FieldLine</div>
          <div class="brand-tag">MARKETING</div>
        </div>
      </div>
      <div class="divider"></div>
      <ul class="contacts">
        <li>
          <svg viewBox="0 0 16 16"><circle cx="8" cy="8" r="7" fill="none" stroke="#8dc03a" stroke-width="1.4"/><path d="M5.5 4.5l1.5 1.6-0.8 1c.6 1.2 1.4 2 2.6 2.6l1-.8 1.6 1.5-1 1.2C7.9 11.4 4.6 8.1 4.4 5.5z" fill="#8dc03a"/></svg>
          +1 555 014 2210
        </li>
        <li>
          <svg viewBox="0 0 16 16"><circle cx="8" cy="8" r="7" fill="none" stroke="#8dc03a" stroke-width="1.4"/><rect x="4" y="5.5" width="8" height="5.5" fill="none" stroke="#8dc03a" stroke-width="1.2"/><path d="M4 5.5l4 3 4-3" fill="none" stroke="#8dc03a" stroke-width="1.2"/></svg>
          <span>hello@<b>mailbox</b>.com</span>
        </li>
        <li>
          <svg viewBox="0 0 16 16"><circle cx="8" cy="8" r="7" fill="none" stroke="#8dc03a" stroke-width="1.4"/><ellipse cx="8" cy="8" rx="3" ry="7" fill="none" stroke="#8dc03a" stroke-width="1"/><path d="M1 8h14M2.5 4.5h11M2.5 11.5h11" stroke="#8dc03a" stroke-width="1"/></svg>
          <span>www.<b>fieldline</b>.com</span>
        </li>
      </ul>
    </header>

    <section class="hero">
      <div class="hero-photo" role="img" aria-label="Photo of colleagues at a desk reviewing charts on a tablet and taking notes"></div>
      <div class="hero-panel">
        <p>Lorem Ipsum</p>
        <strong>has been</strong>
        <p>the industry's</p>
        <strong>standard</strong>
      </div>
    </section>

    <section class="benefits">
      <h2>Benefits Of Advertising With FieldLine</h2>
      <ul class="benefit-list">
        <li><b>Inexpensive:</b> Only $31.00 per month!</li>
        <li><b>Exposure:</b> Our digital signage is placed in only the best/high traffic businesses in your area.</li>
        <li><b>Repetition:</b> Your ad is shown over 3,500 time each month (42,000 times per year)!</li>
        <li><b>Local:</b> We show your ad to consumers in YOUR area. Let us help you do business with the people you want to do business with.</li>
        <li><b>Exclusivity:</b> Only 2 ads per industry.</li>
        <li><b>Lead Generation:</b> We show consumers how to reach you and where to find you.</li>
        <li><b>Brand Awareness:</b> People need to know your business. We make that happen by putting your brand right in front of them.</li>
        <li><b>Digital:</b> Digital advertising has higher retention rates and higher consumer engagement.</li>
      </ul>
    </section>

    <footer class="footer-band"><span>www.<b>fieldline</b>.com</span></footer>
  </main>
</body>
</html>
```